Derek Folsom Resume

Need to update resume with latest position and ensure it stays to 2 pages, may need advice on what to get rid of and simply clean it up, already have a format that i like but am open to change but don't want to spend a fortune

```html
<!DOCTYPE html>
<html lang="en">
<head>
<meta charset="utf-8">
<title>Derek Folsom Resume – Page 2</title>
<link rel="stylesheet" href="https://fonts.googleapis.com/css2?family=Libre+Baskerville:wght@700&family=Open+Sans:wght@400;700&display=swap">
<style>
  :root {
    --navy: #1f3a6e;
    --accent: #16357a;
    --ink: #111111;
    --bar: #ebebeb;
    --paper: #ffffff;
  }
  * { margin: 0; padding: 0; box-sizing: border-box; }
  html, body { width: 946px; height: 1200px; overflow: hidden; background: var(--paper); }
  body {
    font-family: "Open Sans", Tahoma, sans-serif;
    font-size: 13.4px;
    letter-spacing: 0.4px;
    line-height: 18.3px;
    color: var(--ink);
    position: relative;
  }
  .page-header {
    position: absolute; top: 40px; left: 24px; right: 88px;
    display: flex; justify-content: space-between;
    font-family: "Libre Baskerville", Georgia, serif;
    font-variant: small-caps; font-weight: 700;
    font-size: 21px; letter-spacing: 1px; color: var(--navy);
  }
  .content { position: absolute; top: 82px; left: 22px; width: 898px; }
  ul.points { list-style: none; }
  ul.points li {
    position: relative; padding-left: 45px; margin-bottom: 6.4px;
    text-align: justify;
  }
  ul.points li::before {
    content: ""; position: absolute; left: 27px; top: 7px;
    width: 5px; height: 5px; background: var(--ink);
  }
  ul.points b { font-weight: 700; }
  .company {
    text-align: center; font-weight: 700; font-size: 17.4px;
    letter-spacing: 0.2px; line-height: 22px; margin-top: 10px;
  }
  .role-title {
    background: var(--bar); height: 25px; line-height: 25px;
    text-align: center; font-weight: 700; font-size: 16.6px;
    letter-spacing: 0.3px; margin-top: 21px;
  }
  .company + .role-title { margin-top: 9px; }
  .summary { margin: 9px 2px 0; text-align: justify; }
  .highlight {
    text-align: center; font-weight: 700; color: var(--accent);
    letter-spacing: 0.7px; margin: 6.4px 0;
  }
</style>
</head>
<body>
  <header class="page-header">
    <span>Derek W. Folsom</span>
    <span>Page | 2</span>
  </header>

  <main class="content">
    <ul class="points">
      <li><b>Complex Negotiations</b>: Renewed three major contracts resulting in annual revenue of $12 million dollars.</li>
      <li><b>Partner Relationships</b>: Worked closely with system integrators, distributors, and value-added resellers.</li>
      <li><b>Strategic Planning</b>: Created strong nationwide strategic sales programs targeted to the Central Clearing Board.</li>
    </ul>

    <h2 class="company">Vantor Wireless ■ 1999 –2014</h2>

    <section class="role">
      <h3 class="role-title">Client Executive (2012 –2014)</h3>
      <p class="summary">Managed all aspects of national account management including establishing C-level communications, negotiating contracts, selling complex solutions, and increasing revenue and product penetration. Responsible for Civic Safety Bureau, Bureau of Legal Affairs, Legislative Offices, and Bureau of Public Learning.</p>
      <p class="highlight">Sold largest NovaOS solution in Vantor History – 10K Nova phones across Civic Safety Bureau within a 6-month timeframe.</p>
      <ul class="points">
        <li><b>Sales Recognition:</b> Received 2012 President’s Circle Honor due to finishing 2012 at 133% to budget.</li>
        <li><b>Revenue Growth:</b> Consistently overachieved monthly revenue quota.</li>
        <li><b>Market Share:</b> Negotiated multimillion, multiyear contracts to ensure financial contracts were secured in order to provide opportunities for Regional Account Managers to sell within local market.</li>
        <li><b>Solution Selling:</b> Responsible for selling entire portfolio including IaaS, SaaS, SIP, MPLS, and Wireless.</li>
        <li><b>Training &amp; Leadership:</b> Developed, disseminated, and provided training on National Programs to Vantor’s field account managers; offered valuable insight by creating a bi-weekly agency newsletter, which outlined potential gaps and needs.</li>
      </ul>
    </section>

    <section class="role">
      <h3 class="role-title">Regional B2B Sales Manager (2007 – 2012)</h3>
      <p class="summary">Managed a hybrid sales team of 10 enterprise, general business, public sector, and higher education representatives. Focused on increasing revenue with current customers and coached team on best practices for prospecting new business.</p>
      <p class="highlight">Instrumental in 4 of 8 team members achieving President’s Circle in 2010.</p>
      <ul class="points">
        <li><b>President’s Circle:</b> Maintained #1 team ranking out of 40 managers in Northeast area and #2 ranking out of 120 managers nationwide (18 month period).</li>
        <li><b>2011 Results:</b> Achieved 173% to budget in 2011; ranked #1 out of 12 teams in the Mid-Atlantic, #4 out of 120 in U.S.</li>
        <li><b>Southern VA/West VA Turnaround:</b> Transformed struggling Richmond market from bottom-ranked in the Mid-Atlantic to #1 in 2009.</li>
        <li><b>Team Accountability:</b> Managed activities of individual contributors with accountability for quotas, forecasting, funnel management, and account plans.</li>
      </ul>
    </section>

    <section class="role">
      <h3 class="role-title">Indirect Sales Manager (2003 – 2007)</h3>
      <p class="summary">Managed team of 8 account executives overseeing relationships with Signal Shack, TechMart, Brightway, and Volt City. Built and established the local dealer channel in the Virginia markets.</p>
      <p class="highlight">Captured 80% of Signal Shack wireless sales in Virginia market which ranked #1 in country.</p>
      <ul class="points">
        <li><b>Overall Floor Share:</b> Captured a total of 85% of wireless sales, solidifying Vantor as a dominant carrier of choice for each account by building and leveraging productive account relationships.</li>
        <li><b>Market Penetration:</b> Played key role in leading Hampton Roads/Richmond market to one of Vantor’s top-five penetrated markets out of 99 markets nationally, ranking #1 for overall profitability and lowest churn in 2005.</li>
        <li><b>Signal Shack/Dunmore’s:</b> Achieved highest growth in Northeast market for Richmond Signal Shack sales in 2004; placed #1 in Northeast for per-door average in Dunmore’s Clubs in 2005; 25-market area includes Boston, D.C., and New York.</li>
      </ul>
    </section>

    <section class="role">
      <h3 class="role-title">Sales &amp; Merchandising Manager (2002 – 2003)</h3>
      <p class="summary">Teamed with outside temporary agencies and identified and recruited talent; trained, managed, and motivated up to 70 part-time and full-time associates.</p>
      <p class="highlight">Turned around struggling unit and attained #1 ranking in country for sales per hour in 2003.</p>
      <ul class="points">
        <li><b>Floor Share:</b> Achieved over 90% wireless sales in all dealer channels where sales representatives were deployed.</li>
        <li><b>Revenue Results:</b> Generated over $1.5M in revenue in 2003 by developing and delivering solid training that enabled sales associates to excel; over 25% of these employees were promoted to sales and management positions.</li>
      </ul>
    </section>
  </main>
</body>
</html>
```